Landing page for selling a web application used by archeologists

We are selling a web program that professional archeologists use. This program is developed and designed already. But we are now building another website for presenting this web program.
I have uploaded a pdf file that shows the mockup of the future web page. You will also find a folder containing the photos used in the mockup. You can use your own photos for the ones named with "(can be changed)".
There is another folder called "otherPhoto". You can use them if you want to do background or ambiance...
We expect a really clean, serious, and professional design.

You will see in the mockup that there is a first part (main header) followed by 6 subparts presenting the different aspect of the web app. It finishes with the last part presenting ourselves and inviting to test the program.

Here are some links to website designs that go in the direction of what we want.
https://morvani.quillbarrow.com/startup/#home
https://www.tarnpixel-wp. com/mobileapp-landing/
https://en.brovalent.com/
https://assets.plorvik.com/en/klyma-saas-software-landing-html5-page-template-RT4PW9/preview

Don't hesitate to contact me if you need more explanations.
As requested by a designer, I also added 2 print screen of the app that we are selling.
Updates

Feel free to use your own photos for background images for example...

Target Market(s)

Professional archaeologists

Industry/Entity Type

Archeology

Number of Pages Required

1 page

Colors
0054AA
0677BA
7BADD7
CADEEF
E8F1F8
0094D4
00A9DD
6FCCEA
C7EBF8
E9F6FB
FFC000
F8CF3A
FAE287
FDF2CF
FEFAEE

Requirements
Must have
• A professional look that says that our company is large and serious

```html
<!DOCTYPE html>
<html lang="en">
<head>
<meta charset="utf-8">
<title>Fossora – Technology serving archeology</title>
<link href="https://fonts.googleapis.com/css2?family=Bitter:wght@400;500;600&family=Roboto:wght@400;500&display=swap" rel="stylesheet">
<style>
:root{
  --hero:#1f5eab;
  --hero-deep:#174d93;
  --sky:#2196f3;
  --navy:#0d3a73;
  --ink:#1d1d1d;
  --text:#333;
  --dark:#1b3d5a;
  --dark-2:#23506f;
  --foot-a:#1a5cb0;
  --foot-b:#1fa0ee;
  --line:#d9dde3;
  --title-blue:#1e6fc0;
}
*{box-sizing:border-box;margin:0;padding:0}
html,body{width:1200px;height:4988px;overflow:hidden}
body{position:relative;font-family:"Bitter",serif;color:var(--text);background:#fff}
.abs{position:absolute}
.ph{position:absolute;border:1px solid var(--line);background:#fff;padding:10px}
.ph .fill{width:100%;height:100%}
/* hero */
.hero{position:absolute;left:0;top:0;width:1200px;height:640px;background:linear-gradient(135deg,var(--hero) 0%,var(--hero-deep) 100%)}
.brand{position:absolute;display:flex;align-items:center;gap:10px;font-family:"Bitter",serif;font-weight:600;color:#fff;font-size:23px}
.brand i{display:block;width:22px;height:22px;border-radius:50%;background:#6fccea}
.nav{position:absolute;left:428px;top:36px;display:flex;gap:43px;font-size:15px;color:#fff;font-weight:500}
.pill{position:absolute;height:44px;border-radius:22px;background:var(--sky);color:#fff;font-size:14px;font-weight:500;display:flex;align-items:center;justify-content:center}
.hero h1{position:absolute;left:99px;top:196px;font-size:43px;line-height:51px;font-weight:600;color:#fff}
.hero h1 span{color:#6fccea}
.hero .lead{position:absolute;left:99px;top:316px;width:470px;font-size:20px;line-height:31px;color:#fff}
.btn{display:flex;align-items:center;justify-content:center;border-radius:26px;color:#fff;font-weight:500}
/* features */
.section-title{position:absolute;left:0;width:1200px;top:716px;text-align:center;color:var(--title-blue);font-size:29px;font-weight:500}
.feat h2{font-size:35px;font-weight:500;color:var(--ink);margin-bottom:14px}
.feat h3{font-size:21px;font-weight:500;color:var(--ink);line-height:26px;margin-bottom:18px}
.feat .q{font-size:15px;font-weight:500;color:var(--ink);line-height:26px;margin-bottom:16px}
.feat .p{font-size:15px;line-height:26px;color:#333;margin-bottom:28px}
.more{width:146px;height:44px;background:var(--navy);font-size:15px;border-radius:22px}
/* about */
.about{position:absolute;left:0;top:3549px;width:1200px;height:770px;background:linear-gradient(180deg,var(--dark) 0%,var(--dark-2) 100%);color:#fff;text-align:center}
.about h2{position:absolute;left:0;width:1200px;top:62px;font-size:28px;line-height:36px;font-weight:500}
.about .intro{position:absolute;left:250px;width:700px;top:147px;font-size:15px;line-height:26px}
.col{position:absolute;top:244px;width:334px;height:460px;padding:0 24px}
.col.mid{border:1px solid rgba(255,255,255,.6)}
.col svg{display:block;margin:18px auto 0}
.col h4{font-size:22px;font-weight:400;line-height:26px;margin-top:22px;height:62px;display:flex;align-items:center;justify-content:center}
.col p{font-size:13.5px;line-height:25px;margin-top:10px;height:186px}
.outline{width:160px;height:46px;border:2px solid #fff;border-radius:23px;margin:0 auto;font-size:15px;display:flex;align-items:center;justify-content:center}
/* trial */
.trial{position:absolute;left:0;top:4319px;width:1200px;height:290px;background:linear-gradient(180deg,#f2f4f7,#e3e7ec)}
.trial h2{position:absolute;left:0;width:1200px;top:80px;text-align:center;font-size:29px;font-weight:500;color:var(--ink)}
/* footer */
.footer{position:absolute;left:0;top:4560px;width:1200px;height:428px;background:linear-gradient(100deg,var(--foot-a),var(--foot-b));color:#fff;font-family:"Roboto",sans-serif}
.footer h5{font-size:21px;font-weight:500;margin-bottom:20px}
.footer ul{list-style:none;font-size:13.5px;line-height:26px}
.footer li::before{content:"»";margin-right:18px}
.social{display:flex;gap:8px;margin-top:14px}
.social span{width:30px;height:30px;border-radius:50%;background:#fff;display:block}
.copy{position:absolute;left:0;width:1200px;top:370px;text-align:center;font-size:14px}
</style>
</head>
<body>

<header class="hero">
  <div class="brand" style="left:99px;top:30px"><i></i>FOSSORA</div>
  <nav class="nav"><span>Home</span><span>About</span><span>Solution</span><span>Price</span><span>Contacts</span></nav>
  <div class="pill" style="left:900px;top:24px;width:96px">EN ▾</div>
  <div class="pill" style="left:1006px;top:24px;width:96px">Login</div>
  <h1>TECHNOLOGY SERVING<br><span>ARCHEOLOGY</span></h1>
  <p class="lead">Fossora the solution to input, analyse and promote the archaeological heritage</p>
  <div class="btn abs" style="left:99px;top:406px;width:181px;height:50px;background:var(--sky);font-size:16px">Get Started</div>
  <div class="abs" role="img" aria-label="Two desktop monitors showing the application screens" style="left:540px;top:140px;width:660px;height:420px;background:radial-gradient(ellipse at center,#8fb4dc 0%,#3f78bd 55%,transparent 75%)"></div>
  <svg class="abs" style="left:0;top:520px" width="1200" height="120" viewBox="0 0 1200 120"><path d="M0 110 C260 110 420 30 640 30 C880 30 980 90 1200 90 L1200 120 L0 120Z" fill="#fff"/></svg>
</header>

<h2 class="section-title">HOW ITS WORK</h2>

<!-- Entry -->
<div class="feat abs" style="left:99px;top:828px;width:330px">
  <h2>FossoraEntry</h2>
  <h3>Capture of archaeological information</h3>
  <p class="q">How to make more, faster, with the same amount of resources ?</p>
  <p class="p">-&gt; Fossora as force Multiplier</p>
  <div class="btn more">More details</div>
</div>
<div class="ph" style="left:443px;top:801px;width:695px;height:379px"><div class="fill" role="img" aria-label="Monitor and tablet showing the data entry screen" style="background:linear-gradient(135deg,#dfe6ee,#9fb3c8)"></div></div>

<!-- Analysis -->
<div class="ph" style="left:99px;top:1260px;width:302px;height:187px"><div class="fill" role="img" aria-label="Line charts of discoveries per period" style="background:linear-gradient(135deg,#eef2f8,#c6d3e6)"></div></div>
<div class="ph" style="left:99px;top:1459px;width:302px;height:188px"><div class="fill" role="img" aria-label="Scatter plot of correspondence analysis" style="background:linear-gradient(135deg,#f6f6f6,#e0e0e0)"></div></div>
<div class="ph" style="left:418px;top:1260px;width:289px;height:387px"><div class="fill" role="img" aria-label="Heat map with dendrogram" style="background:linear-gradient(160deg,#fbe3a0,#f29b3c 55%,#c23a1f)"></div></div>
<div class="feat abs" style="left:776px;top:1285px;width:340px">
  <h2>FossoraAnalysis</h2>
  <h3>Analysis of archaeological information</h3>
  <p class="q">How to detect hidden relationships, make sense of the information and preserve the big picture?</p>
  <p class="p">-&gt; Fossora as an intuitive solution</p>
  <div class="btn more">More details</div>
</div>

<!-- Publication -->
<div class="feat abs" style="left:97px;top:1765px;width:450px">
  <h2>FossoraPublication</h2>
  <h3>Publication of archaeological information</h3>
  <p class="q">How to publish in a scientific format and find the information scattered among multiple publications in Pdf format?</p>
  <p class="p">-&gt; Fossora as a tool for publishing<br>and searching information</p>
  <div class="btn more">More details</div>
</div>
<div class="ph" style="left:604px;top:1732px;width:518px;height:368px"><div class="fill" role="img" aria-label="Tablets displaying a published excavation report" style="background:linear-gradient(135deg,#e9ecef,#a9b4bf)"></div></div>

<!-- View -->
<div class="ph" style="left:99px;top:2200px;width:623px;height:354px"><div class="fill" role="img" aria-label="Photograph of a lakeside medieval castle" style="background:linear-gradient(180deg,#9dbde0 0%,#c9d6e0 45%,#8b8474 70%,#4f5e66 100%)"></div></div>
<div class="feat abs" style="left:774px;top:2193px;width:340px">
  <h2>FossoraView</h2>
  <h3>Promotion of the archaeological heritage</h3>
  <p class="q">How to render the archaeological heritage accessible to the general public, as well as to the educational and tourist sectors?</p>
  <p class="p">-&gt; Fossora as a mobilizing and unifying power</p>
  <div class="btn more">More details</div>
</div>

<!-- Forum -->
<div class="feat abs" style="left:99px;top:2692px;width:450px">
  <h2>FossoraForum</h2>
  <h3>Staying in touch with the community</h3>
  <p class="q">How to connect among specialists and exchange ideas across borders and languages ?</p>
  <p class="p">-&gt; FossoraForum as a solution for<br>multilingual specialist networking</p>
  <div class="btn more">More details</div>
</div>
<div class="ph" style="left:604px;top:2657px;width:518px;height:367px"><div class="fill" role="img" aria-label="Network illustration of connected specialists" style="background:radial-gradient(circle,#e4eefb 0%,#ffffff 75%)"></div></div>

<!-- Archive -->
<div class="ph" style="left:99px;top:3144px;width:623px;height:316px"><div class="fill" role="img" aria-label="Photograph of stacked paper archives" style="background:linear-gradient(90deg,#5a4a3c 0%,#a08a70 40%,#d8dde3 70%,#eef0f3 100%)"></div></div>
<div class="feat abs" style="left:776px;top:3144px;width:340px">
  <h2>FossoraArchive</h2>
  <h3>Retrieval of information</h3>
  <p class="q">How to find information quickly within archives in various formats (pdf, xls, doc, etc.) ?</p>
  <p class="p">-&gt; Fossora as a solution for dispersed information</p>
  <div class="btn more">More details</div>
</div>

<!-- About -->
<section class="about">
  <h2>FOSSORA: INNOVATIVE, RELIABLE, AT<br>THE CUTTING EDGE OF TECHNOLOGY</h2>
  <p class="intro">Founded by a Swiss team of computer engineers and statistical analysts, Fossora places innovation at the service of success. Its vocation: to offer the latest computer tools to the world of archaeology in order to facilitate and promote the work of archaeologists</p>
  <div class="col" style="left:99px">
    <svg width="110" height="110" viewBox="0 0 110 110" fill="none" stroke="#fff" stroke-width="3"><circle cx="55" cy="30" r="14"/><path d="M15 80 L40 60 L55 70 L70 60 L95 80 M30 90 L55 72 L80 90"/></svg>
    <h4>The expertise and security of a Swiss company</h4>
    <p>We bring together the most advanced technical engineering skills to deploy the right solutions for the most demanding problems. Big data input and processing, scalability, statistic analysis, deep learning, machine learning are our daily routine</p>
    <div class="outline">Learn More</div>
  </div>
  <div class="col mid" style="left:430px">
    <svg width="110" height="110" viewBox="0 0 110 110" fill="none" stroke="#2196f3" stroke-width="3"><circle cx="55" cy="45" r="24"/><path d="M55 32 V58 M62 37 H51 A5 5 0 0 0 51 47 H59 A5 5 0 0 1 59 57 H48 M15 85 H50 L70 75 M95 20 H80"/></svg>
    <h4>Affordable prices</h4>
    <p>Budgets in archaeology are often limited. Reaching a large number of users allows advanced technological services that are usually very expensive to be offered at very low prices.</p>
    <div class="outline">Learn More</div>
  </div>
  <div class="col" style="left:766px">
    <svg width="110" height="110" viewBox="0 0 110 110" fill="none" stroke="#fff" stroke-width="3"><circle cx="55" cy="55" r="42"/><circle cx="55" cy="55" r="12"/><circle cx="55" cy="55" r="24" stroke-dasharray="10 6"/></svg>
    <h4>Ongoing developments</h4>
    <p>Accompanied by professional archaeologists, we are continually shaping Fossora to meet their precise needs and expectations. We are always listening to new development proposals in order to solve the problems that archeologists face</p>
    <div class="outline">Learn More</div>
  </div>
</section>

<!-- Trial -->
<section class="trial">
  <h2>Get now a free 3-month trial of Fossora</h2>
  <div class="btn abs" style="left:518px;top:152px;width:164px;height:52px;background:var(--sky);font-size:20px;font-family:Roboto,sans-serif;font-weight:400">Contact us</div>
</section>

<!-- Footer -->
<footer class="footer">
  <svg class="abs" style="left:0;top:-1px" width="1200" height="80" viewBox="0 0 1200 80"><path d="M0 0 H1200 V20 C900 0 700 60 420 60 C200 60 80 40 0 30Z" fill="#e6e9ee"/></svg>
  <div class="abs" style="left:99px;top:136px;width:240px">
    <div class="brand" style="position:static;margin-bottom:14px"><i></i>FOSSORA</div>
    <p style="font-size:12.5px;line-height:25px">Duis aute irure dolor in reprehenderit in voluptate velit esse cillum dolore eu fugiat nulla pariatur.</p>
    <div class="social"><span></span><span></span><span></span><span></span></div>
  </div>
  <div class="abs" style="left:367px;top:140px"><h5>Menu</h5><ul><li>Home</li><li>About</li><li>Solution</li><li>Price</li><li>Contacts</li></ul></div>
  <div class="abs" style="left:588px;top:140px"><h5>Help Link</h5><ul><li>Terms&amp;condtions</li><li>Privacy Policy</li><li>About Us</li><li>Support</li><li></li></ul></div>
  <div class="abs" style="left:871px;top:140px;width:240px"><h5>Contact us</h5>
    <ul style="font-size:13.5px">
      <li style="list-style:none">Address :<br>Lorem ipsum dolor sit amet,<br>consectetur adipiscing</li>
      <li>+1 888 888 8888</li>
      <li>info@fossora.com</li>
    </ul>
  </div>
  <p class="copy">© 2022 Fossora. | All Rights Reserved | Terms and Conditions</p>
</footer>

</body>
</html>
```